IT’S NOT A CLEANING, IT’S YOUR LIFE! TOP TEN REASONS WHY THIS IS NOT JUST A “CLEANING”

We made a list for our patients to let them know why our hygiene appointments are different than other cleanings. Since this is a lot of information, we would like it easily readable within 4-5 feet but we do not want the post to be HUGE. Please see below:

IT’S NOT A CLEANING, IT’S YOUR LIFE!
TOP TEN REASONS WHY THIS IS NOT JUST A “CLEANING”

10. We make you look better. Healthy teeth and gums are more attractive. Recent studies
show that the smile is the first thing people notice and that people with better looking teeth
are more confident and successful.

9. We can relieve your headaches. During your hygiene visit we evaluate for serious bite
issues, many of which lead to muscle soreness, headaches, and migraines.

8. We check for oral cancer. Oral cancer kills 1 person per hour 24 hours a day. The death rate for oral cancer is higher than cancers we routinely hear about such as cervical, thyroid and skin cancer.

7. We make you smell better. During your hygiene visit we eliminate many of the germs that live under your gum tissue and cause bad breath.

6. We save you money. By utilizing the latest dental technology (digital x-rays, mouth
cameras, and magnification glasses) we can help with early detection of tooth and gum
problems and save you the cost of gum surgery, root canals, and implants.

5. We clean in places you cannot. We clean under the gum line and between teeth where
most of the germs hide and cause dental disease. 40% of the bacteria in your mouth lives in
between your teeth.

4. We prevent pain. We identify tooth decay that can lead to nerve involvement and pain,
root canal, and tooth loss.

3. We save your teeth. Most tooth loss is from periodontal/gum disease. At each visit we
evaluate the health of your gums and bone with our periodontal screening. Periodontal
disease, like high blood pressure, is symptomless until it is in advanced stages.

2. We protect your loved ones. Studies have proven that the bacteria that cause dental
disease can be transmitted from person to person. Think about that the next time you kiss
someone!

1. We prolong life. Researchers have linked the inflammation and infection found in the
mouth to heart attacks, strokes, and Alzheimer’s. By reducing infection in your mouth we can
greatly improve your overall health!

```html
<!DOCTYPE html>
<html lang="en">
<head>
<meta charset="utf-8">
<title>It's Not a Cleaning, It's Your Life</title>
<link href="https://fonts.googleapis.com/css2?family=Didact+Gothic&family=Questrial&display=swap" rel="stylesheet">
<style>
  :root {
    --frame: #ffffff;
    --wood-light: #a8662c;
    --wood-mid: #8a4d1d;
    --wood-dark: #5e2f0e;
    --seam: rgba(30, 12, 2, 0.85);
    --band: rgba(14, 7, 3, 0.86);
    --ink: #ffffff;
  }
  html, body {
    margin: 0;
    padding: 0;
    width: 776px;
    height: 1200px;
    overflow: hidden;
    background: var(--frame);
  }
  .poster {
    position: relative;
    width: 776px;
    height: 1200px;
    background: var(--frame);
    font-family: "Didact Gothic", "Questrial", sans-serif;
    color: var(--ink);
  }
  .wood-panel {
    position: absolute;
    left: 14px;
    top: 14px;
    width: 748px;
    height: 1172px;
    overflow: hidden;
    background:
      linear-gradient(90deg, rgba(0,0,0,0.18), rgba(255,255,255,0.04) 30%, rgba(0,0,0,0.08) 60%, rgba(255,255,255,0.05) 85%, rgba(0,0,0,0.2)),
      linear-gradient(180deg, var(--wood-mid), var(--wood-light) 30%, var(--wood-mid) 55%, var(--wood-light) 75%, var(--wood-dark));
  }
  .plank-seams,
  .header-band {
    position: absolute;
    left: 0;
    top: 0;
  }
  .headline {
    position: absolute;
    left: 46px;
    top: 70px;
    margin: 0;
    font-family: "Questrial", sans-serif;
    font-weight: 400;
    font-size: 30.5px;
    line-height: 36px;
    letter-spacing: 0.5px;
    text-transform: uppercase;
    white-space: nowrap;
  }
  .subhead {
    position: absolute;
    left: 46px;
    top: 110px;
    margin: 0;
    font-family: "Questrial", sans-serif;
    font-weight: 400;
    font-size: 24.5px;
    line-height: 30px;
    letter-spacing: 0.4px;
    text-transform: uppercase;
    white-space: nowrap;
  }
  .reasons {
    list-style: none;
    margin: 0;
    padding: 0;
  }
  .reason {
    position: absolute;
    left: 46px;
    width: 700px;
    margin: 0;
    font-size: 19px;
    line-height: 22.5px;
    text-shadow: 0 0 2px rgba(0,0,0,0.35);
  }
</style>
</head>
<body>
<div class="poster">
  <div class="wood-panel" role="img" aria-label="Warm brown wood grain background">
    <svg class="plank-seams" width="748" height="1172" viewBox="0 0 748 1172" aria-hidden="true">
      <rect x="0" y="292" width="748" height="4" fill="var(--seam)"/>
      <rect x="0" y="466" width="748" height="5" fill="var(--seam)"/>
      <rect x="0" y="650" width="748" height="5" fill="var(--seam)"/>
      <rect x="0" y="957" width="748" height="4" fill="var(--seam)"/>
    </svg>
    <svg class="header-band" width="748" height="180" viewBox="0 0 748 180" aria-hidden="true">
      <polygon points="0,32 748,0 748,142 0,174" fill="var(--band)"/>
    </svg>
  </div>

  <h1 class="headline">It’s not a cleaning, it’s your life!</h1>
  <h2 class="subhead">Top ten reasons why this is not just a “cleaning”</h2>

  <ol class="reasons">
    <li class="reason" style="top:216px">10. We make you look better. Healthy teeth and gums are more attractive.<br>Recent studies show that the smile is the first thing people notice and that people with better looking teeth are more confident and successful.</li>
    <li class="reason" style="top:326px">9. We can relieve your headaches. During your hygiene visit we evaluate for serious bite issues, many of which lead to muscle soreness, headaches, and migraines.</li>
    <li class="reason" style="top:393px">8. We check for oral cancer. Oral cancer kills 1 person per hour 24 hours a day. The death rate for oral cancer is higher than cancers we routinely hear about such as cervical, thyroid and skin cancer.</li>
    <li class="reason" style="top:498px">7. We make you smell better. During your hygiene visit we eliminate many of the germs that live under your gum tissue and cause bad breath.</li>
    <li class="reason" style="top:578px">6. We save you money. By utilizing the latest dental technology (digital x-rays, mouth cameras, and magnification glasses) we can help with early detection of tooth and gum problems and save you the cost of gum surgery, root canals, and implants.</li>
    <li class="reason" style="top:680px">5. We clean in places you cannot. We clean under the gum line and between teeth where most of the germs hide and cause dental disease. 40% of the bacteria in your mouth lives in between your teeth.</li>
    <li class="reason" style="top:781px">4. We prevent pain. We identify tooth decay that can lead to nerve involvement and pain, root canal, and tooth loss.</li>
    <li class="reason" style="top:865px">3. We save your teeth. Most tooth loss is from periodontal/gum disease. At each visit we evaluate the health of your gums and bone with our periodontal screening. Periodontal disease, like high blood pressure, is symptomless until it is in advanced stages.</li>
    <li class="reason" style="top:985px">2. We protect your loved ones. Studies have proven that the bacteria that cause dental disease can be transmitted from person to person. Think about that the next time you kiss someone</li>
    <li class="reason" style="top:1062px">1. We prolong life. Researchers have linked the inflammation and infection found in the mouth to heart attacks, strokes, and Alzheimer’s. By reducing infection in your mouth we can greatly improve your overall health!</li>
  </ol>
</div>
</body>
</html>
```